General Contractors need a new Crisp updated Card Design

We need a new business card design for our company of 25 years based in Toronto call Pollvarn Building Inc. : Our goal is to be the leading commercial contractors in Toronto by providing exceptional value to our clients. We work very hard to deliver professional, quality, service in conjunction with consistent price competitiveness to all of our clients on every single project.

Target Market(s)

Design & Build Clients

Industry/Entity Type

Construction Company

Contact Information for Business Card

Address:
18 West Marlow Field Road, Unit 17, Dunmore Vale, ON, K7T 2M9
Office: 905-218-6937

Pollvarns Logo
Employee Job Description
Employee Cell Phone #
Employee Email
www.pollvarn.example

Colors

Designer to choose colors to be used in the design.

Requirements
Must have
• Quote Company Saying:
• "Professional. Quality. Service."
Nice to have
• New Crisp up to date look. simple & fresh ( Not to Busy)
Should not have
• NO BLUE PRINTS ON THE BUSINESS CARDS

```html
<!DOCTYPE html>
<html lang="en">
<head>
<meta charset="utf-8">
<title>Pollvarn Building Inc. — Business Cards</title>
<link rel="stylesheet" href="https://fonts.googleapis.com/css2?family=Lato:wght@400;700&family=Cormorant+Garamond:wght@500&display=swap">
<style>
  :root {
    --green: #00634f;
    --green-deep: #005543;
    --sage: #a9bcad;
    --mist: #e4ece8;
    --paper: #ffffff;
    --stage: #ebedec;
    --edge: #c9d3cf;
  }
  * { margin: 0; padding: 0; box-sizing: border-box; }
  html, body { width: 1200px; height: 900px; overflow: hidden; }
  body {
    background: var(--stage);
    position: relative;
    font-family: "Lato", "Helvetica Neue", Arial, sans-serif;
    color: var(--green);
  }
  .card {
    position: absolute;
    width: 515px;
    height: 298px;
    overflow: hidden;
    background: var(--paper);
    border: 1px solid var(--edge);
    box-shadow: 0 1px 3px rgba(0,0,0,0.12);
  }
  .card--back-a { left: 71px;  top: 137px; }
  .card--back-b { left: 615px; top: 137px; }
  .card--back-c { left: 71px;  top: 463px; }
  .card--front  { left: 615px; top: 463px; }

  .back-field { position: absolute; inset: 0; }
  .back-field--a {
    background:
      linear-gradient(200deg, var(--green) 0%, var(--green) 30%, var(--mist) 62%, var(--paper) 78%, var(--sage) 100%);
  }
  .back-field--b {
    background:
      linear-gradient(155deg, var(--green) 0%, var(--green) 22%, var(--paper) 55%, var(--mist) 80%, var(--green) 100%);
  }
  .back-field--c {
    background:
      radial-gradient(ellipse 70% 60% at 50% 60%, var(--paper) 0%, var(--mist) 45%, rgba(228,236,232,0) 75%),
      linear-gradient(180deg, var(--green) 0%, var(--green-deep) 55%, var(--sage) 100%);
  }

  .brand {
    position: absolute; left: 33px; top: 40px;
    display: flex; align-items: center; gap: 10px;
  }
  .brand__square { width: 56px; height: 56px; background: var(--green); flex: none; }
  .brand__name {
    font-weight: 700;
    font-size: 24px;
    line-height: 1.05;
    text-transform: uppercase;
    letter-spacing: 0.5px;
    color: var(--green);
  }

  .person {
    position: absolute; left: 0; right: 0; top: 147px;
    text-align: center;
  }
  .person__name { font-weight: 700; font-size: 16px; letter-spacing: 0.3px; }
  .person__role { font-size: 14px; margin-top: 2px; }

  .contact {
    position: absolute; left: 36px; top: 208px;
    list-style: none; font-size: 12.5px; line-height: 16px;
  }
  .contact__item { display: flex; align-items: center; gap: 5px; }
  .contact__icon { width: 10px; height: 10px; flex: none; }

  .office {
    position: absolute; right: 40px; top: 208px;
    text-align: right; font-size: 12.5px; line-height: 16px;
    font-style: normal;
  }
  .office__web { font-weight: 700; }

  .tagline {
    position: absolute; left: 0; right: 0; bottom: 0; height: 34px;
    background: var(--green);
    color: var(--paper);
    font-family: "Cormorant Garamond", Georgia, serif;
    font-weight: 500;
    font-size: 13px;
    letter-spacing: 7.4px;
    white-space: nowrap;
    display: flex; align-items: center;
    padding-left: 38px;
  }
</style>
</head>
<body>

  <section class="card card--back-a" aria-label="Card back">
    <div class="back-field back-field--a" role="img" aria-label="Large angled brand-mark decoration in green, white and sage"></div>
  </section>

  <section class="card card--back-b" aria-label="Card back">
    <div class="back-field back-field--b" role="img" aria-label="Large angled brand-mark decoration, shifted crop, in green and white"></div>
  </section>

  <section class="card card--back-c" aria-label="Card back">
    <div class="back-field back-field--c" role="img" aria-label="Large brand-mark decoration with sage base band"></div>
  </section>

  <section class="card card--front" aria-label="Card front">
    <div class="brand">
      <span class="brand__square"></span>
      <span class="brand__name">Pollvarn<br>Building Inc.</span>
    </div>

    <div class="person">
      <p class="person__name">DANIEL HARTWELL</p>
      <p class="person__role">managing director</p>
    </div>

    <ul class="contact">
      <li class="contact__item">
        <svg class="contact__icon" viewBox="0 0 10 10"><rect x="0.5" y="0.5" width="9" height="9" fill="none" stroke="#a9bcad"/><path d="M2 3.2h6v3.8H2z M2 3.2l3 2.2 3-2.2" fill="none" stroke="#00634f" stroke-width="0.8"/></svg>
        d.hartwell@pollvarn.example
      </li>
      <li class="contact__item">
        <svg class="contact__icon" viewBox="0 0 10 10"><rect x="0.5" y="0.5" width="9" height="9" fill="none" stroke="#a9bcad"/><rect x="3.5" y="2" width="3" height="6" rx="0.5" fill="none" stroke="#00634f" stroke-width="0.8"/></svg>
        905 441 7720
      </li>
      <li class="contact__item">
        <svg class="contact__icon" viewBox="0 0 10 10"><rect x="0.5" y="0.5" width="9" height="9" fill="none" stroke="#a9bcad"/><path d="M3 2.5c-0.8 0.6-0.8 2.5 1.2 4.3 1.8 1.5 2.8 1 3.2 0.6l-1-1-0.8 0.5c-0.6-0.3-1.3-1-1.6-1.6l0.5-0.8z" fill="#00634f"/></svg>
        905 218 6937
      </li>
    </ul>

    <address class="office">
      18 West Marlow Field Road, Unit 17<br>
      Dunmore Vale, ON, K7T 2M9<br>
      <span class="office__web">www.pollvarn.example</span>
    </address>

    <p class="tagline">PROFESSIONAL. QUALITY. SERVICE.</p>
  </section>

</body>
</html>
```